2018 Vision Board Workshop

I need to promote this workshop on both an 8.5x11 sheet and a 5x7 card. I do have a logo that needs to be present. I'd like to stay true to my branded colors. The flyer needs to project the excitement of a new year and the possibilities of what a person can create, produce, explore in their lives by putting it all on a vision board. Creating the vision of what you want will inspire you to achieve your goals and dreams. Looking at your vision board each day will propel you into taking action as you chart your course to achieve what you truly want.
The flyer needs to have the following information:
The workshop date and time - Sat., Jan. 13, 2018, 10:30-1:30
The location is - Atrium 47B, 2864 Birchwood Vale Rd, Colorado Springs, Co 80417
in the FORGE Room
My name and contact information - Mara Vollbeck
Text and voice 303-417-6652
Email - mara@brightwell-daily-craft.com
Website - brightwell-daily-craft.com
The fee is $45. All materials are provided.

My company is called Brightwell Daily Craft. I am a Life Coach, author, speaker and workshop leader.\ I wrote this program, Brightwell Daily Craft to teach concepts and supporting skills for living with more happiness, satisfaction and fulfillment. Thanks for reading this!! Mara

Target Market(s)

Primarily women, educated, motivated, proactive in their own lives and well being

Font styles to use
Other font styles liked:
• I have been using Century Gothic. I'm open to new ideas.

Requirements
Must have
• The Brightwell Daily Craft logo
• The flyer needs to have the following information:
• The workshop date and time - Sat., Jan. 13, 2018, 10:30-1:30
• The location is - Atrium 47B, 2864 Birchwood Vale Rd, Colorado Springs, Co 80417
• in the FORGE Room
• My name and contact information - Mara Vollbeck
• Text and voice 303-417-6652
• Email - mara@brightwell-daily-craft.com
• Website - brightwell-daily-craft.com
• The fee is $45. All materials are provided.
Nice to have
• The Brightwell Daily Craft branded colors in the design
• Images of vision boards

```html
<!DOCTYPE html>
<html lang="en">
<head>
<meta charset="utf-8">
<title>2018 Vision Board Workshop</title>
<link href="https://fonts.googleapis.com/css2?family=Open+Sans:wght@600;700&family=Questrial&display=swap" rel="stylesheet">
<style>
  :root {
    --brand-green: #8dc63f;
    --band-green: #9acd3c;
    --ink: #1a1a1a;
    --body-ink: #4a4a4a;
    --white: #ffffff;
    --hero-cream: #f1efd2;
    --hero-mint: #bfe0c4;
    --hero-teal: #7fcdb6;
    --hero-coral: #e9825a;
    --hero-sun: #f5dd8c;
  }
  * { box-sizing: border-box; margin: 0; padding: 0; }
  html, body { width: 979px; height: 1200px; overflow: hidden; background: var(--white); }
  .flyer {
    position: relative;
    width: 979px;
    height: 1200px;
    background: var(--white);
    font-family: "Questrial", "Century Gothic", sans-serif;
    color: var(--body-ink);
  }
  .hero {
    position: absolute;
    left: 0; top: 0;
    width: 979px; height: 600px;
    background:
      radial-gradient(ellipse 220px 180px at 470px 250px, rgba(233,130,90,0.75), transparent 70%),
      radial-gradient(ellipse 260px 220px at 560px 380px, rgba(245,221,140,0.8), transparent 70%),
      radial-gradient(ellipse 260px 260px at 120px 300px, rgba(127,205,182,0.75), transparent 70%),
      radial-gradient(ellipse 300px 240px at 820px 380px, rgba(191,224,196,0.9), transparent 70%),
      radial-gradient(ellipse 400px 300px at 500px 100px, rgba(241,239,210,1), transparent 80%),
      linear-gradient(180deg, var(--hero-cream) 0%, var(--hero-mint) 70%, var(--white) 100%);
    -webkit-mask-image: linear-gradient(180deg, #000 78%, transparent 100%);
    mask-image: linear-gradient(180deg, #000 78%, transparent 100%);
  }
  .headline {
    position: absolute;
    left: 151px; top: 282px;
    font-family: "Open Sans", sans-serif;
    font-weight: 700;
    font-size: 64px;
    line-height: 88px;
    color: var(--white);
    letter-spacing: 0.5px;
  }
  .fee-seal {
    position: absolute;
    left: 782px; top: 482px;
    width: 164px; height: 164px;
  }
  .fee-seal svg { position: absolute; inset: 0; }
  .fee-seal p {
    position: absolute;
    inset: 0;
    display: flex; align-items: center; justify-content: center;
    text-align: center;
    color: var(--white);
    font-size: 18px;
    line-height: 25px;
  }
  .brand-name {
    position: absolute;
    left: 0; width: 979px; top: 652px;
    text-align: center;
    font-size: 48px;
    color: var(--brand-green);
  }
  .intro {
    position: absolute;
    left: 55px; width: 870px; top: 746px;
    text-align: center;
    font-size: 20px;
    line-height: 26px;
  }
  .workshop-title {
    position: absolute;
    left: 0; width: 979px; top: 838px;
    display: flex; align-items: center; justify-content: center; gap: 24px;
    font-size: 32px;
    color: var(--brand-green);
  }
  .workshop-title::before, .workshop-title::after {
    content: ""; width: 133px; height: 1.5px; background: #333;
  }
  .date-box {
    position: absolute;
    left: 63px; top: 898px;
    width: 865px; height: 66px;
    border: 2px solid var(--brand-green);
    display: flex; align-items: center; justify-content: center;
    font-size: 32px;
    color: var(--ink);
  }
  .venue {
    position: absolute;
    left: 0; width: 979px; top: 992px;
    text-align: center;
    font-size: 20px;
    line-height: 25px;
    color: #555;
  }
  .contact-band {
    position: absolute;
    left: 0; top: 1066px;
    width: 979px; height: 134px;
    background: var(--band-green);
    color: var(--white);
  }
  .contact-name {
    position: absolute;
    left: 0; width: 979px; top: 16px;
    text-align: center;
    font-size: 40px;
  }
  .contact-list {
    position: absolute;
    left: 0; width: 979px; top: 76px;
    list-style: none;
    display: flex; justify-content: center; gap: 28px;
    font-family: "Open Sans", sans-serif;
    font-weight: 600;
    font-size: 19px;
  }
  .contact-list li { display: flex; align-items: center; gap: 8px; }
  .contact-list svg { width: 20px; height: 20px; }
</style>
</head>
<body>
<main class="flyer">
  <div class="hero" role="img" aria-label="Joyful woman with arms outstretched in soft winter light with bokeh and snowflakes"></div>
  <h1 class="headline">WHAT YOU THINK IS<br>WHAT YOU CREATE</h1>

  <div class="fee-seal">
    <svg viewBox="0 0 164 164" aria-hidden="true">
      <g fill="var(--brand-green)">
        <rect x="28" y="28" width="108" height="108" transform="rotate(0 82 82)"/>
        <rect x="28" y="28" width="108" height="108" transform="rotate(11.25 82 82)"/>
        <rect x="28" y="28" width="108" height="108" transform="rotate(22.5 82 82)"/>
        <rect x="28" y="28" width="108" height="108" transform="rotate(33.75 82 82)"/>
        <rect x="28" y="28" width="108" height="108" transform="rotate(45 82 82)"/>
        <rect x="28" y="28" width="108" height="108" transform="rotate(56.25 82 82)"/>
        <rect x="28" y="28" width="108" height="108" transform="rotate(67.5 82 82)"/>
        <rect x="28" y="28" width="108" height="108" transform="rotate(78.75 82 82)"/>
      </g>
    </svg>
    <p>The fee is $45.<br>All materials<br>are provided.</p>
  </div>

  <div class="brand-name">Brightwell Daily Craft</div>

  <p class="intro">Creating the vision of what you want will inspire you to achieve your goals and dreams. Looking at your vision board each day will propel you into taking action as you chart your course to achieve what you truly want.</p>

  <h2 class="workshop-title">2018 Vision Board Workshop</h2>

  <div class="date-box">Saturay, January 13, 2018, 10:30-1:30</div>

  <p class="venue">Atrium 47B, 2864 Birchwood Vale<br>Rd, Colorado Springs, Co 80417</p>

  <footer class="contact-band">
    <div class="contact-name">Mara Vollbeck</div>
    <ul class="contact-list">
      <li>
        <svg viewBox="0 0 20 20" aria-hidden="true"><circle cx="10" cy="10" r="8.5" fill="none" stroke="#fff" stroke-width="1.5"/><rect x="5.5" y="7" width="9" height="6" fill="none" stroke="#fff" stroke-width="1.3"/><path d="M5.5 7l4.5 3.5L14.5 7" fill="none" stroke="#fff" stroke-width="1.3"/></svg>
        mara@brightwell-daily-craft.com
      </li>
      <li>
        <svg viewBox="0 0 20 20" aria-hidden="true"><circle cx="10" cy="10" r="8.5" fill="none" stroke="#fff" stroke-width="1.5"/><path d="M7 5.5c-1 .5-1.5 1.5-1 3 .8 2.5 3 4.8 5.5 5.8 1.3.5 2.5 0 3-1l-1.8-1.6-1.3.8c-1.2-.6-2.2-1.6-2.8-2.8l.8-1.3z" fill="#fff"/></svg>
        303-417-6652
      </li>
      <li>
        <svg viewBox="0 0 20 20" aria-hidden="true"><circle cx="10" cy="10" r="8.5" fill="none" stroke="#fff" stroke-width="1.5"/><circle cx="10" cy="10" r="5" fill="none" stroke="#fff" stroke-width="1.2"/><ellipse cx="10" cy="10" rx="2.2" ry="5" fill="none" stroke="#fff" stroke-width="1.2"/><path d="M5 10h10" stroke="#fff" stroke-width="1.2"/></svg>
        www.brightwell-daily-craft.com
      </li>
    </ul>
  </footer>
</main>
</body>
</html>
```